Brixel capital

We lend hard money loans for fixer upper homes and new constructions.Easy Financing on Fix Homes

Target Market(s)

People that need loans & money to buy a Home

Industry/Entity Type

Mortgage Lender

Font styles to use
Serif
Sans Serif

Colors
ffffff
9ccb3b

Requirements
Must have
• Catchy, modern, Clean
Nice to have
• Easy to read

```html
<!DOCTYPE html>
<html lang="en">
<head>
<meta charset="utf-8">
<title>Brixel capital — Stationery</title>
<link href="https://fonts.googleapis.com/css2?family=Open+Sans:wght@400;600;700&display=swap" rel="stylesheet">
<style>
  :root {
    --brand-green: #9ccb3b;
    --deep-green: #4cae3a;
    --pale-green: #e4f1c9;
    --paper: #ffffff;
    --backdrop: #eceeed;
    --ink: #4a4f4c;
    --muted: #7d837f;
  }
  * { box-sizing: border-box; margin: 0; padding: 0; }
  html, body { width: 1200px; height: 900px; overflow: hidden; }
  body {
    background: var(--backdrop);
    font-family: "Open Sans", Arial, sans-serif;
    color: var(--ink);
    position: relative;
  }
  .sheet {
    position: absolute;
    background: var(--paper);
    box-shadow: 0 6px 18px rgba(0,0,0,0.12);
    overflow: hidden;
  }
  .wave { position: absolute; left: 0; bottom: 0; width: 100%; }
  .brand {
    display: flex; align-items: center; gap: 8px;
    font-weight: 700; color: var(--brand-green);
    white-space: nowrap;
  }
  .brand-mark { display: block; background: var(--brand-green); }
  .contact {
    position: absolute; text-align: right;
    font-size: 10px; line-height: 1.45; color: var(--ink);
  }

  /* Letterhead */
  .letterhead { left: 330px; top: 40px; width: 350px; height: 490px; }
  .letterhead .brand { position: absolute; top: 40px; left: 0; right: 0; justify-content: center; font-size: 20px; }
  .letterhead .brand-mark { width: 14px; height: 14px; }
  .letterhead .contact { right: 28px; bottom: 40px; }

  /* Envelope */
  .envelope { left: 330px; top: 570px; width: 540px; height: 280px; }
  .envelope .brand { position: absolute; top: 32px; left: 36px; font-size: 24px; }
  .envelope .brand-mark { width: 16px; height: 16px; }
  .envelope .contact { right: 32px; bottom: 30px; font-size: 11px; }

  /* Folder */
  .folder {
    left: 725px; top: 40px; width: 435px; height: 500px;
    background: linear-gradient(160deg, #a2cf3f 0%, var(--brand-green) 55%, #8fc232 100%);
    display: flex; align-items: center; justify-content: center;
  }
  .folder .brand { color: var(--paper); font-size: 44px; }
  .folder .brand-mark { width: 30px; height: 30px; background: var(--paper); }

  /* Business cards */
  .card { left: 40px; width: 260px; height: 150px; }
  .card-front { top: 330px; display: flex; align-items: center; justify-content: center; }
  .card-front .brand { font-size: 22px; position: relative; z-index: 1; }
  .card-front .brand-mark { width: 14px; height: 14px; }
  .card-back { top: 510px; }
  .card-back .brand { position: absolute; top: 14px; left: 0; right: 0; justify-content: center; font-size: 15px; }
  .card-back .brand-mark { width: 10px; height: 10px; }
  .card-back .divider { position: absolute; top: 48px; left: 0; right: 0; height: 1px; background: #cfd4d0; }
  .person { position: absolute; left: 16px; top: 60px; }
  .person-name { font-size: 11px; font-weight: 700; color: var(--ink); }
  .person-role { font-size: 8px; color: var(--muted); }
  .card-details { position: absolute; left: 128px; top: 58px; list-style: none; font-size: 8px; line-height: 1.75; }
  .card-details li { display: flex; align-items: center; gap: 5px; }
  .card-details svg { width: 9px; height: 9px; flex: none; }
</style>
</head>
<body>

  <section class="sheet letterhead" aria-label="Letterhead">
    <svg class="wave" viewBox="0 0 350 200" height="200" preserveAspectRatio="none" aria-hidden="true">
      <defs>
        <linearGradient id="lh-soft" x1="0" y1="0" x2="1" y2="0">
          <stop offset="0" stop-color="#b8db72"/><stop offset="1" stop-color="#ffffff" stop-opacity="0"/>
        </linearGradient>
        <linearGradient id="lh-deep" x1="0" y1="0" x2="1" y2="0">
          <stop offset="0" stop-color="#4cae3a"/><stop offset="0.6" stop-color="#9ccb3b" stop-opacity="0.6"/><stop offset="1" stop-color="#ffffff" stop-opacity="0"/>
        </linearGradient>
      </defs>
      <path d="M0 40 C90 20 170 60 230 120 C270 160 320 190 350 200 L0 200 Z" fill="url(#lh-soft)" opacity="0.7"/>
      <path d="M0 90 C80 70 150 110 210 160 C240 185 290 200 350 200 L0 200 Z" fill="url(#lh-deep)" opacity="0.8"/>
    </svg>
    <div class="brand"><span class="brand-mark"></span>Brixel capital</div>
    <address class="contact">
      418 Linden Park Avenue Atlanta, GA 30309<br>
      info@brixelcapital.com<br>
      www.brixelcapital.com
    </address>
  </section>

  <section class="sheet envelope" aria-label="Envelope">
    <svg class="wave" viewBox="0 0 540 200" height="200" preserveAspectRatio="none" aria-hidden="true">
      <defs>
        <linearGradient id="env-soft" x1="0" y1="0" x2="1" y2="0">
          <stop offset="0" stop-color="#b8db72"/><stop offset="1" stop-color="#ffffff" stop-opacity="0"/>
        </linearGradient>
        <linearGradient id="env-deep" x1="0" y1="0" x2="1" y2="0">
          <stop offset="0" stop-color="#4cae3a"/><stop offset="0.5" stop-color="#9ccb3b" stop-opacity="0.5"/><stop offset="1" stop-color="#ffffff" stop-opacity="0"/>
        </linearGradient>
      </defs>
      <path d="M0 20 C140 0 260 60 360 140 C420 185 480 200 540 200 L0 200 Z" fill="url(#env-soft)" opacity="0.7"/>
      <path d="M0 70 C120 60 220 110 300 170 C340 195 400 200 460 200 L0 200 Z" fill="url(#env-deep)" opacity="0.8"/>
    </svg>
    <div class="brand"><span class="brand-mark"></span>Brixel capital</div>
    <address class="contact">
      418 Linden Park Avenue Atlanta, GA 30309<br>
      info@brixelcapital.com<br>
      www.brixelcapital.com
    </address>
  </section>

  <section class="sheet folder" aria-label="Presentation folder">
    <div class="brand"><span class="brand-mark"></span>Brixel capital</div>
  </section>

  <section class="sheet card card-front" aria-label="Business card front">
    <svg class="wave" viewBox="0 0 260 150" height="150" preserveAspectRatio="none" aria-hidden="true">
      <defs>
        <linearGradient id="cf-soft" x1="0" y1="0" x2="1" y2="0">
          <stop offset="0" stop-color="#b8db72"/><stop offset="1" stop-color="#ffffff" stop-opacity="0"/>
        </linearGradient>
      </defs>
      <path d="M0 0 L110 0 C60 40 30 90 0 150 Z" fill="url(#cf-soft)" opacity="0.6"/>
      <path d="M260 150 L150 150 C200 120 230 80 260 40 Z" fill="#9ccb3b" opacity="0.35"/>
    </svg>
    <div class="brand"><span class="brand-mark"></span>Brixel capital</div>
  </section>

  <section class="sheet card card-back" aria-label="Business card back">
    <svg class="wave" viewBox="0 0 260 150" height="150" preserveAspectRatio="none" aria-hidden="true">
      <path d="M0 95 C50 100 90 125 120 150 L0 150 Z" fill="#9ccb3b" opacity="0.55"/>
    </svg>
    <div class="brand"><span class="brand-mark"></span>Brixel capital</div>
    <div class="divider"></div>
    <div class="person">
      <p class="person-name">Name Surname</p>
      <p class="person-role">Director</p>
    </div>
    <ul class="card-details">
      <li><svg viewBox="0 0 10 10" aria-hidden="true"><rect width="10" height="10" fill="#9ccb3b"/><path d="M3 2 L4.5 2 L5 4 L4 4.6 Q4.8 6 6 6.2 L6.6 5.2 L8 5.8 L8 7.4 Q4 8 2.6 3.4 Z" fill="#fff"/></svg>+00 987 654 321</li>
      <li><svg viewBox="0 0 10 10" aria-hidden="true"><rect width="10" height="10" fill="#4aa6d8"/><path d="M5 1.8 A2.2 2.2 0 0 1 7.2 4 C7.2 5.6 5 8.2 5 8.2 C5 8.2 2.8 5.6 2.8 4 A2.2 2.2 0 0 1 5 1.8 Z" fill="#fff"/></svg>Elm Lane 7-KD London</li>
      <li><svg viewBox="0 0 10 10" aria-hidden="true"><rect width="10" height="10" fill="#f08a24"/><rect x="2" y="3" width="6" height="4" fill="none" stroke="#fff" stroke-width="0.8"/><path d="M2 3 L5 5.3 L8 3" fill="none" stroke="#fff" stroke-width="0.8"/></svg>info@brixelcapital.com</li>
      <li><svg viewBox="0 0 10 10" aria-hidden="true"><rect width="10" height="10" fill="#8a8f8c"/><circle cx="5" cy="5" r="2.8" fill="none" stroke="#fff" stroke-width="0.8"/><path d="M2.2 5 H7.8 M5 2.2 V7.8" stroke="#fff" stroke-width="0.6"/></svg>www.brixelcapital.com</li>
    </ul>
  </section>

</body>
</html>
```